Book Cover Design - Uncovering Weight Loss Secrets

I need a book cover design for a book called 'Folding The Map'. It is a book that goes through all of the secrets to weight loss, without any crazy shakes or workouts or pills or potions. The book is really focused on helping people understand that Weight loss is simple and has more to do with our mindset as well as the food we were eating. It is about taking personal responsibility not looking for the next fancy revolutionary product that is going to help them magically melt the fat away. The book is pragmatic in nature and breaks down in simple terms how we can lose weight and keep it off for the rest of our lives. It shows the user that it is simple to lose weight, but it takes effort. They should stop looking for a quick fix when it comes to weight loss but instead eat healthy for the rest of their lives.
The book is intended to be hard-hitting no holds barred approach. The book has the same title as my business name. I will attach the current logo that we use in the business. This doesn't need to be on the front of the book maybe at the back down the bottom somewhere.
I am looking to have both an e-book cover and a standard printed book cover.
I don't have any colours in mind, my logo can be adapted to be different colours or just white.
The message that I am wanting people to feel when they see my book, is that all these Weightloss fads are a joke, that I know the secrets that will get them to their weight loss goal even if they fail at everything else before.
On the cover it should say the following.
FOLDING THE MAP
Uncovering the Weight Loss Secrets
The big companies have been trying to keep hidden for years!
COLIN MAYHEW
People who have failed many times trying to lose weight & need help
Weight Loss

```html
<!DOCTYPE html>
<html lang="en">
<head>
<meta charset="utf-8">
<title>Folding The Map – Book Cover</title>
<link href="https://fonts.googleapis.com/css2?family=Lato:wght@300;700;900&family=Open+Sans:wght@700;800&family=Caveat+Brush&display=swap" rel="stylesheet">
<style>
  :root {
    --page-bg: #e6e6e6;
    --cover-bg: #262626;
    --cover-bg-light: #333333;
    --gold: #9a8155;
    --green: #5fae2e;
    --white: #f4f4f4;
    --photo-blue: #3d5fa8;
    --photo-blue-dark: #2c4684;
  }
  * { margin: 0; padding: 0; box-sizing: border-box; }
  html, body {
    width: 1200px;
    height: 800px;
    overflow: hidden;
    background: var(--page-bg);
  }
  .canvas {
    position: relative;
    width: 1200px;
    height: 800px;
  }
  .cover {
    position: absolute;
    left: 406px;
    top: 93px;
    width: 398px;
    height: 607px;
    background: linear-gradient(160deg, var(--cover-bg-light) 0%, var(--cover-bg) 55%, #202020 100%);
    overflow: hidden;
    text-align: center;
    color: var(--white);
  }
  .author-photo {
    position: absolute;
    left: 178px;
    top: 200px;
    width: 220px;
    height: 407px;
    background: linear-gradient(180deg,
      rgba(38, 38, 38, 0) 0%,
      rgba(61, 95, 168, 0.55) 30%,
      var(--photo-blue) 55%,
      var(--photo-blue-dark) 100%);
  }
  .tagline {
    position: absolute;
    top: 19px;
    left: 0;
    width: 100%;
    font-family: "Lato", sans-serif;
    font-size: 15.5px;
    line-height: 19.5px;
    letter-spacing: -0.3px;
    text-transform: uppercase;
    padding-left: 10px;
  }
  .tagline .light { font-weight: 300; }
  .tagline .bold { font-weight: 700; }
  .title {
    position: absolute;
    top: 112px;
    left: 0;
    width: 100%;
  }
  .title-main {
    display: block;
    font-family: "Lato", sans-serif;
    font-weight: 700;
    font-size: 76px;
    line-height: 1;
    color: var(--gold);
    letter-spacing: -0.5px;
  }
  .title-sub {
    display: block;
    font-family: "Caveat Brush", cursive;
    font-size: 46px;
    line-height: 1;
    color: var(--green);
    margin-top: -2px;
    transform: rotate(-3deg);
  }
  .headline {
    position: absolute;
    top: 268px;
    left: 0;
    width: 100%;
    font-family: "Open Sans", sans-serif;
    font-weight: 800;
    font-size: 38px;
    line-height: 47px;
    letter-spacing: -0.5px;
    text-transform: uppercase;
    color: var(--white);
  }
  .author-name {
    position: absolute;
    top: 549px;
    left: 0;
    width: 100%;
    font-family: "Lato", sans-serif;
    font-weight: 700;
    font-size: 22px;
    letter-spacing: 6px;
    padding-left: 6px;
    color: var(--white);
  }
</style>
</head>
<body>
<main class="canvas">
  <section class="cover">
    <div class="author-photo" role="img" aria-label="Photograph of the author in a blue shirt, hand at chin, arms folded"></div>

    <p class="tagline">
      <span class="light">For</span> <span class="bold">losing all the weight you want</span><br>
      <span class="light">&amp; keeping it off forever</span><br>
      <span class="bold">No matter what you have tried in the past</span>
    </p>

    <h1 class="title">
      <span class="title-main">FOLDING</span>
      <span class="title-sub">The Map</span>
    </h1>

    <p class="headline">Weight<br>Loss<br>Secrets</p>

    <p class="author-name">COLIN MAYHEW</p>
  </section>
</main>
</body>
</html>
```